***Flyer*** TOLMARDE AUTO TRANSPORT *** Flyer***

I need a flyer design that explain my auto transport business... the design must be eye catching and draws a persons attention at first site. We Tow Cars locally in the City of Houston for a flat rate of $75... We ask that the designer make the $75 standout so it will catch the attention of the reader. Much of the content writing can be gather from my website tolmardeautotransport.example - the designer can use his own images to express his design work... I will attach the logo and some samples of some reason business and post cards designs. If you chose you can also add these images in your designs if it will help.

Size of flyer is 8"x11" front and back

Automotive

Requirements
Must have
• $75 or $75.00
• (555) 274-3186
• service@tolmardeautotransport.example
• www.tolmardeautotransport.example
Nice to have
• WE REALLY WANT TO EARN YOUR BUSINESS
• Note: Please look at my website for content writing to create your flyer.

```html
<!DOCTYPE html>
<html lang="en">
<head>
<meta charset="utf-8">
<title>Tolmarde Auto Transport – $75 Flat Rate Flyer</title>
<link href="https://fonts.googleapis.com/css2?family=Archivo+Narrow:wght@700&family=Nunito:wght@900&family=Roboto+Condensed:wght@700&display=swap" rel="stylesheet">
<style>
  :root{
    --red:#c8141f;
    --red-deep:#8e0c14;
    --orange:#e8791c;
    --gold:#d9a021;
    --navy:#1d1c7e;
    --navy-dark:#100f4a;
    --white:#ffffff;
    --ink:#111111;
    --grey:#8a8a8a;
    --curve-red:#d21f26;
  }
  html,body{margin:0;padding:0;overflow:hidden;background:var(--white);}
  .flyer{position:relative;width:879px;height:1200px;overflow:hidden;background:var(--white);}
  .flyer__backdrop{
    position:absolute;left:11px;top:11px;width:855px;height:1000px;
    background:
      radial-gradient(ellipse at 60% 12%, rgba(217,160,33,.85) 0%, rgba(232,121,28,.5) 30%, transparent 60%),
      linear-gradient(90deg,var(--red) 0%,#e0441c 40%,var(--orange) 60%,#d8401c 85%,var(--red-deep) 100%);
  }
  .flyer__art{position:absolute;left:0;top:0;width:879px;height:1000px;}
  .curve-text{font-family:"Archivo Narrow",sans-serif;font-weight:700;font-size:31px;fill:var(--curve-red);}
  .curve-text .price{fill:var(--navy);}
  .reputation{
    position:absolute;left:0;top:880px;width:879px;
    font-family:"Roboto Condensed",sans-serif;font-weight:700;color:var(--white);
  }
  .reputation__line1{position:absolute;left:73px;top:0;font-size:24px;white-space:nowrap;}
  .reputation__line2{position:absolute;left:118px;top:22px;font-size:24px;white-space:nowrap;}
  .reputation__city{font-size:41px;vertical-align:-3px;}
  .slogan{
    position:absolute;left:0;width:879px;top:944px;text-align:center;
    font-family:"Roboto Condensed",sans-serif;font-weight:700;font-size:40px;
    color:var(--white);letter-spacing:-.5px;white-space:nowrap;
  }
  .footer-band{position:absolute;left:11px;top:988px;width:855px;height:170px;background:var(--white);}
  .footer-band__edge{position:absolute;left:866px;top:1000px;width:7px;height:160px;background:var(--grey);}
  .footer-band__strip{position:absolute;left:11px;top:1158px;width:855px;height:16px;background:var(--red-deep);}
  .footer-chevrons{position:absolute;left:11px;top:988px;width:855px;height:186px;}
  .brand{
    position:absolute;left:30px;top:1012px;width:290px;text-align:center;
    font-family:"Roboto Condensed",sans-serif;font-weight:700;font-size:28px;line-height:1.05;color:var(--ink);
  }
  .contact{
    position:absolute;left:30px;top:1082px;width:290px;margin:0;padding:0;list-style:none;text-align:center;
    font-family:"Roboto Condensed",sans-serif;font-weight:700;font-size:14px;line-height:1.5;color:var(--ink);
  }
  .contact__phone{font-size:20px;color:var(--red);line-height:1.25;}
  .tow-illustration{
    position:absolute;left:430px;top:1000px;width:420px;height:145px;border-radius:6px;
    background:linear-gradient(90deg,rgba(210,31,38,.12),rgba(210,31,38,.28));
  }
</style>
</head>
<body>
<main class="flyer">
  <div class="flyer__backdrop" role="img" aria-label="Road map of the Houston area in warm red and orange tones"></div>

  <svg class="flyer__art" viewBox="0 0 879 1000">
    <defs>
      <linearGradient id="dollarFill" x1="0" y1="0" x2="0" y2="1">
        <stop offset="0" stop-color="#d9a021"/>
        <stop offset=".5" stop-color="#e8791c"/>
        <stop offset="1" stop-color="#e05a1a"/>
      </linearGradient>
      <path id="ringPath" d="M253 778 A385 385 0 1 1 688 146"/>
    </defs>

    <circle class="badge" cx="443" cy="443" r="425" fill="var(--white)"/>

    <text class="dollar-sign" x="440" y="830" text-anchor="middle" role="img" aria-label="Large dollar sign filled with a Houston road map"
          font-family="Roboto Condensed, sans-serif" font-weight="700" font-size="930" fill="url(#dollarFill)">$</text>

    <text class="curve-text">
      <textPath href="#ringPath" textLength="1240" lengthAdjust="spacingAndGlyphs">We offer a flat rate of <tspan class="price">$75.00</tspan> to move your vehicle and guarantee your vehicle gets moved in 24 hours or less.</textPath>
    </text>

    <g class="rate" font-family="Nunito, sans-serif" font-weight="900" font-size="590">
      <g fill="var(--navy-dark)">
        <text x="120" y="722" transform="translate(9 9)">7</text>
        <text x="470" y="668" transform="translate(9 9)">5</text>
        <text x="120" y="722" transform="translate(4 4)">7</text>
        <text x="470" y="668" transform="translate(4 4)">5</text>
      </g>
      <g fill="var(--navy)">
        <text x="120" y="722">7</text>
        <text x="470" y="668">5</text>
      </g>
    </g>
  </svg>

  <div class="reputation">
    <span class="reputation__line1">Our reputation has long established us</span>
    <span class="reputation__line2">as one of the best tow truck services in <span class="reputation__city">Houston!</span></span>
  </div>
  <div class="slogan">WE REALLY WANT TO EARN YOUR BUSINESS!!</div>

  <div class="footer-band"></div>
  <div class="footer-band__edge"></div>
  <svg class="footer-chevrons" viewBox="0 0 855 186" aria-hidden="true">
    <polygon points="300,0 345,0 430,85 345,170 300,170 385,85" fill="var(--red)"/>
    <polygon points="345,0 372,0 452,85 372,170 345,170 430,85" fill="var(--red-deep)"/>
  </svg>
  <div class="footer-band__strip"></div>

  <div class="brand">TOLMARDE<br>AUTO TRANSPORT</div>
  <ul class="contact">
    <li class="contact__phone">(555) 274-3186</li>
    <li class="contact__email">service@tolmardeautotransport.example</li>
    <li class="contact__web">www.tolmardeautotransport.example</li>
  </ul>
  <div class="tow-illustration" role="img" aria-label="Red line drawing of a tow truck loading a car onto its flatbed"></div>
</main>
</body>
</html>
```